agricultural technology company needs business cards*

design a business card that represents our business well. please see our website: vastrelbyfieldseal.com.au
professional, simple, clean lines, not complicated or floral.....

```html
<!DOCTYPE html>
<html lang="en">
<head>
<meta charset="utf-8">
<title>Vastrelby FieldSeal — Business Card</title>
<link rel="stylesheet" href="https://fonts.googleapis.com/css2?family=Archivo:wght@700&family=Josefin+Sans:wght@300;400&display=swap">
<style>
  :root {
    --navy: #1f2d5c;
    --green: #2fa04a;
    --lime: #94c13d;
    --paper: #f4f4f2;
    --ink-grey: #7d7f84;
    --backdrop: #dcdcda;
  }
  * { margin: 0; padding: 0; box-sizing: border-box; }
  html, body { width: 1200px; height: 801px; overflow: hidden; }
  body {
    background: var(--backdrop);
    position: relative;
    font-family: "Josefin Sans", sans-serif;
  }
  .card {
    position: absolute;
    top: 240px;
    width: 540px;
    height: 310px;
    overflow: hidden;
    box-shadow: 0 10px 30px rgba(0,0,0,0.18);
  }
  .card--front { left: 40px; background: var(--paper); }
  .card--back { left: 620px; background: var(--navy); }
  .card__shape { position: absolute; inset: 0; width: 100%; height: 100%; }

  .wordmark {
    position: absolute;
    font-family: "Archivo", sans-serif;
    font-weight: 700;
    line-height: 0.92;
    letter-spacing: -0.5px;
  }
  .card--front .wordmark { left: 30px; top: 92px; font-size: 40px; color: var(--navy); }
  .card--back .wordmark { left: 32px; bottom: 34px; font-size: 54px; color: #ffffff; }

  .person { position: absolute; left: 30px; top: 196px; }
  .person__name { font-size: 18px; color: var(--green); font-weight: 400; }
  .person__role { font-size: 12px; color: var(--ink-grey); font-weight: 300; margin-top: 2px; }

  .contacts { position: absolute; left: 30px; bottom: 20px; list-style: none; }
  .contacts li {
    display: flex; align-items: center; gap: 8px;
    font-size: 11px; color: var(--ink-grey); font-weight: 300;
    line-height: 17px;
  }
  .contacts .contacts__web { color: var(--navy); font-weight: 400; }
  .contact-icon { width: 12px; height: 12px; flex: none; }

  .address {
    position: absolute; right: 26px; top: 168px;
    font-size: 12px; line-height: 17px; color: var(--ink-grey); font-weight: 300;
    text-align: right;
  }
</style>
</head>
<body>

  <section class="card card--front" aria-label="Business card front">
    <svg class="card__shape" viewBox="0 0 540 310" preserveAspectRatio="none" aria-hidden="true">
      <polygon points="180,0 540,0 540,170" fill="var(--navy)"/>
    </svg>
    <div class="wordmark">Vastrelby<br>FieldSeal</div>
    <div class="person">
      <p class="person__name">Marek Oduya</p>
      <p class="person__role">Founder &amp; Co-Owner</p>
    </div>
    <ul class="contacts">
      <li>
        <svg class="contact-icon" viewBox="0 0 12 12" aria-hidden="true"><circle cx="6" cy="6" r="6" fill="var(--green)"/><path d="M4 3.2 5 4.6 4.5 5.3c.4.9 1.1 1.6 2 2l.7-.5 1.4 1-.5 1c-2.4-.2-4.3-2.1-4.5-4.5z" fill="#fff"/></svg>
        1300 482 610
      </li>
      <li>
        <svg class="contact-icon" viewBox="0 0 12 12" aria-hidden="true"><circle cx="6" cy="6" r="6" fill="var(--green)"/><rect x="3" y="4" width="6" height="4.2" fill="none" stroke="#fff" stroke-width="0.8"/><path d="M3 4l3 2.3L9 4" fill="none" stroke="#fff" stroke-width="0.8"/></svg>
        info@vastrelbyfieldseal.com.au
      </li>
      <li class="contacts__web">
        <svg class="contact-icon" viewBox="0 0 12 12" aria-hidden="true"><circle cx="6" cy="6" r="6" fill="var(--green)"/><circle cx="6" cy="6" r="3" fill="none" stroke="#fff" stroke-width="0.8"/><path d="M3 6h6M6 3c-1.2 1.6-1.2 4.4 0 6M6 3c1.2 1.6 1.2 4.4 0 6" fill="none" stroke="#fff" stroke-width="0.6"/></svg>
        vastrelbyfieldseal.com.au
      </li>
    </ul>
    <p class="address">14 Harlow Rd,<br>Kelmscott Bay WA 6099</p>
  </section>

  <section class="card card--back" aria-label="Business card back">
    <svg class="card__shape" viewBox="0 0 540 310" preserveAspectRatio="none" aria-hidden="true">
      <line x1="150" y1="0" x2="540" y2="200" stroke="var(--lime)" stroke-width="6"/>
    </svg>
    <div class="wordmark">Vastrelby<br>FieldSeal</div>
  </section>

</body>
</html>
```